Flyer Vacation Gift Certificate

I need to create a beautiful flyer 8.5 x 11 PDF format flyer design. <br/><br/>Instructions:<br/>The flyer will really be a gift voucher for a las vegas vacation getaway. So must have a Las Vegas Theme exciting fun<br/><br/>The voucher should have two modules that will be editable. <br/>Must have a "Compliments Of" area and also must have an "Exclusively For" area<br/><br/>Keep in mind that this flyer will be printed so keep that in mind :)<br/><br/>Here the is the content for the vacation voucher:<br/><br/>There is no doubt that Las Vegas is one of the hottest travel destinations around the world. In fact, some people would even go as far as<br/>saying that perhaps it is THE hottest place to visit. Enjoy up to 4 nights of resort/casino accommodations in exciting Las Vegas, NV. Millions of people travel to this exciting city each year to enjoy its thrills. Thanks to the business you received this certificate from, now you can enjoy exciting Las Vegas, NV too!<br/><br/>Features:<br/>*Travel 7 Days A Week<br/>*Stay Your Choice Of Nights (1-4 Nights)<br/>*Good For Two Adults & Two Children<br/>*Pay Just The Taxes & Fees<br/>*Multiple Travel Date Requests Allowed<br/>*Fully Transferable To Another Person<br/>*Just A 30 Days Advance Notice Required<br/>*You Will Have 12 Months To Complete Travel After Redemption<br/><br/>HOW CAN WE DO THIS?<br/><br/>We contract with the world leading hotel chains and resorts to help them fill their otherwise empty rooms.<br/><br/>We help fill empty rooms which the hotels, resorts and cruise lines turn into additional revenue from other areas of their property and future bookings.<br/><br/>Hotels rarely experience full occupancy, yet they remain open, providing rooms and services at fixed costs. So when hotels give out their rooms by partnering with marketing companies like us, they might miss out on the room fee, but they already didn't have that in the first place, at least now they have the opportunity to gain a customer for their in-house restaurants, room service, their casinos, an extra day stay, future bookings, etc.<br/><br/>VIEW ALL THE DETAILS OF THIS SPECIAL OFFER AND REDEEM ONLINE AT <br/>WWW.TOPAZVOUCHERDESK.COM<br/><br/>Certificate ID # 47261-38504<br/>Expires 02/29/2020<br/><br/><br/>*terms and conditions apply see website for details<br/><br/>KEEP IN MIND THE EXAMPLES I AM UPLOADING ARE SIMPLY TO SHOW YOU THAT THEY CONTAIN THE "COMPLIMENTS OF" AND "EXCLUSIVELY FOR" ELEMENTS. THESE MUST BE INCLUDED IN NEW DESIGN. PLEASE ONLY USE THE CONTENT I PROVIDED IN BRIEF, DONT USE CONTENT FROM EXAMPLES.

Target Market(s)

CONSUMERS THAT HAVE BEEN REWARDED WITH A VACATION CERTIFICATE FOR DOING BUSINESS WITH A COMPANY.

COMPANIES USE THESE AS MARKETING INCENTIVES TO ATTRACT MORE CUSTOMERS AND TO REWARD LOYALTY, ETC.

Industry/Entity Type

Travel Industry

Colors

Designer to choose colors to be used in the design.

Requirements
Must have
• I need to create a beautiful flyer 8.5 x 11 PDF format flyer design.
• Instructions:
• The flyer will really be a gift voucher for a las vegas vacation getaway. So must have a Las Vegas Theme exciting fun
• The voucher should have two modules that will be editable.
• Must have a "Compliments Of" area and also must have an "Exclusively For" area
• Keep in mind that this flyer will be printed so keep that in mind :)
• Here the is the content for the vacation voucher:
• There is no doubt that Las Vegas is one of the hottest travel destinations around the world. In fact, some people would even go as far as
• saying that perhaps it is THE hottest place to visit. Enjoy up to 4 nights of resort/casino accommodations in exciting Las Vegas, NV. Millions of people travel to this exciting city each year to enjoy its thrills. Thanks to the business you received this certificate from, now you can enjoy exciting Las Vegas, NV too!
• Features:
• *Travel 7 Days A Week
• *Stay Your Choice Of Nights (1-4 Nights)
• *Good For Two Adults & Two Children
• *Pay Just The Taxes & Fees
• *Multiple Travel Date Requests Allowed
• *Fully Transferable To Another Person
• *Just A 30 Days Advance Notice Required
• *You Will Have 12 Months To Complete Travel After Redemption
• HOW CAN WE DO THIS?
• We contract with the world leading hotel chains and resorts to help them fill their otherwise empty rooms.
• We help fill empty rooms which the hotels, resorts and cruise lines turn into additional revenue from other areas of their property and future bookings.
• Hotels rarely experience full occupancy, yet they remain open, providing rooms and services at fixed costs. So when hotels give out their rooms by partnering with marketing companies like us, they might miss out on the room fee, but they already didn't have that in the first place, at least now they have the opportunity to gain a customer for their in-house restaurants, room service, their casinos, an extra day stay, future bookings, etc.
• VIEW ALL THE DETAILS OF THIS SPECIAL OFFER AND REDEEM ONLINE AT
• WWW.TOPAZVOUCHERDESK.COM
• Certificate ID # 47261-38504
• Expires 02/29/2020
• *terms and conditions apply see website for details
• KEEP IN MIND THE EXAMPLES I AM UPLOADING ARE SIMPLY TO SHOW YOU THAT THEY CONTAIN THE "COMPLIMENTS OF" AND "EXCLUSIVELY FOR" ELEMENTS. THESE MUST BE INCLUDED IN NEW DESIGN. PLEASE ONLY USE THE CONTENT I PROVIDED IN BRIEF, DONT USE CONTENT FROM EXAMPLES.
Nice to have
• EXCITING LAS VEGAS IMAGES THAT MAKE SOMEONE WANT TO GO THERE

```html
<!DOCTYPE html>
<html lang="en">
<head>
<meta charset="utf-8">
<title>Las Vegas Vacation Gift Certificate</title>
<link href="https://fonts.googleapis.com/css2?family=Montserrat:wght@600;700&family=Raleway:wght@300;400;500&family=Oswald:wght@500&display=swap" rel="stylesheet">
<style>
  :root {
    --page-bg: #eceae6;
    --paper: #f7f8fa;
    --brand-blue: #3d6aa6;
    --brand-blue-dark: #2f5a94;
    --ink: #333a44;
    --muted: #6b7078;
    --panel-light: #e2e3e7;
    --panel-mid: #bbbcc0;
    --panel-fold: #5f6166;
    --white: #ffffff;
    --logo-red: #c8313a;
  }
  * { box-sizing: border-box; margin: 0; padding: 0; }
  html, body { width: 1200px; height: 989px; overflow: hidden; background: var(--page-bg); }
  body { position: relative; font-family: "Raleway", sans-serif; color: var(--ink); }

  .certificate {
    position: absolute; left: 266px; top: 20px; width: 668px; height: 950px;
    background: var(--paper); overflow: hidden;
    box-shadow: 0 2px 10px rgba(0,0,0,.12);
  }

  .hero-photo {
    position: absolute; left: 0; top: 0; width: 668px; height: 263px;
    background:
      radial-gradient(ellipse at 35% 75%, rgba(240,180,90,.75), transparent 45%),
      radial-gradient(ellipse at 70% 85%, rgba(90,140,190,.6), transparent 40%),
      linear-gradient(180deg, #3f5f8e 0%, #5a73a0 30%, #6a6a7c 55%, #4a3a38 80%, #2c2628 100%);
  }

  .courtesy-card {
    position: absolute; left: 463px; top: 0; width: 184px; height: 173px;
    background: var(--white); text-align: center; padding-top: 16px;
  }
  .courtesy-card .eyebrow {
    font-family: "Raleway", sans-serif; font-weight: 500; font-size: 15px;
    line-height: 17px; color: var(--brand-blue); letter-spacing: .5px;
  }
  .sponsor-name {
    display: flex; align-items: center; justify-content: center; gap: 5px;
    margin-top: 9px; font-family: "Raleway", sans-serif; font-weight: 500;
    font-size: 15px; color: var(--brand-blue-dark);
  }
  .sponsor-name .mark { width: 10px; height: 10px; background: var(--logo-red); }
  .courtesy-card .lines { margin-top: 20px; font-size: 12px; line-height: 19px; color: var(--ink); }
  .courtesy-card .lines .lead { font-weight: 500; }

  .intro-band {
    position: absolute; left: 0; top: 263px; width: 643px; height: 74px;
    background: var(--brand-blue); color: var(--white);
    font-size: 8.6px; line-height: 11.7px; text-align: center;
    padding: 11px 24px 0 24px;
  }

  .section-tab {
    position: absolute; left: 0; height: 31px; width: 236px;
    background: var(--brand-blue); color: var(--white);
    clip-path: polygon(0 0, 93% 0, 100% 50%, 93% 100%, 0 100%);
    font-family: "Montserrat", sans-serif; font-weight: 700; font-size: 13px;
    line-height: 31px; padding-left: 20px; letter-spacing: .2px;
  }
  .tab-how { top: 352px; }
  .tab-features { top: 496px; }
  .tab-terms { top: 603px; }

  .how-copy {
    position: absolute; left: 21px; top: 392px; width: 636px;
    font-size: 10px; line-height: 13px; color: var(--ink);
  }

  .feature-list {
    position: absolute; top: 536px; list-style: none;
    font-size: 10.2px; line-height: 13.2px; color: var(--ink);
  }
  .feature-list li { padding-left: 10px; position: relative; }
  .feature-list li::before {
    content: ""; position: absolute; left: 0; top: 5px; width: 4px; height: 4px;
    border-radius: 50%; background: var(--brand-blue);
  }
  .features-left { left: 21px; }
  .features-right { left: 242px; top: 534px; }

  .terms-copy {
    position: absolute; left: 21px; top: 644px; width: 320px;
    font-size: 6.2px; line-height: 8.6px; color: var(--muted); text-transform: uppercase;
  }

  .redeem-banner {
    position: absolute; left: 360px; top: 601px; width: 308px; height: 115px;
    background: var(--brand-blue); color: var(--white);
    clip-path: polygon(14% 0, 100% 0, 100% 100%, 14% 100%, 0 50%);
    text-align: right; padding: 23px 41px 0 0;
  }
  .redeem-banner .call { font-size: 10.6px; line-height: 13px; letter-spacing: .3px; }
  .redeem-banner .details {
    margin-top: 14px; font-family: "Montserrat", sans-serif; font-weight: 600;
    font-size: 10px; line-height: 13px;
  }

  .compliments-panel {
    position: absolute; left: 0; top: 704px; width: 317px; height: 246px;
    background: var(--panel-light);
  }
  .fold-strip { position: absolute; left: 317px; top: 704px; }
  .exclusive-panel {
    position: absolute; left: 340px; top: 740px; width: 328px; height: 210px;
    background: var(--panel-mid);
  }
  .panel-label {
    position: absolute; font-family: "Raleway", sans-serif; font-weight: 500;
    font-size: 12px; letter-spacing: .5px; color: #1f2227;
  }
  .compliments-panel .panel-label { left: 21px; top: 22px; }
  .exclusive-panel .panel-label { left: 0; width: 100%; text-align: center; top: 14px; }
</style>
</head>
<body>
  <main class="certificate">
    <div class="hero-photo" role="img" aria-label="Night skyline of the Las Vegas Strip with lit resorts, replica Eiffel Tower and fountains"></div>

    <aside class="courtesy-card">
      <p class="eyebrow">THIS CERTIFICATE IS<br>COMPLIMENTS OF</p>
      <p class="sponsor-name"><span class="mark"></span>Beacon Reach Pro</p>
      <div class="lines">
        <p class="lead">Certificate Courtesy Of</p>
        <p>Text Line 2</p>
        <p>Text Line 3</p>
      </div>
    </aside>

    <p class="intro-band">There is no doubt that Las Vegas is one of the hottest travel destinations around the world. In fact, some people would even go as far as saying that perhaps it is THE hottest place to visit. Enjoy up to 4 nights of resort/casino accommodations in exciting Las Vegas, NV. Millions of people travel to this exciting city each year to enjoy its thrills. Thanks to the business you received this certificate from, now you can enjoy exciting Las Vegas, NV too!</p>

    <h2 class="section-tab tab-how">HOW CAN WE DO THIS?</h2>
    <div class="how-copy">
      <p>We contract with the world leading hotel chains and resorts to help them fill their otherwise empty rooms. We help fill empty rooms which the hotels, resorts and cruise lines turn into additional revenue from other areas of their property and future bookings.</p>
      <p>Hotels rarely experience full occupancy, yet they remain open, providing rooms and services at fixed costs. So when hotels give out their rooms by partnering with marketing companies like us, they might miss out on the room fee, but they already didn't have that in the first place, at least now they have the opportunity to gain a customer for their in-house restaurants, room service, their casinos, an extra day stay, future bookings, etc.</p>
    </div>

    <h2 class="section-tab tab-features">FEATURES:</h2>
    <ul class="feature-list features-left">
      <li>Travel 7 Days A Week</li>
      <li>Stay Your Choice Of Nights (1-4 Nights)</li>
      <li>Good For Two Adults &amp; Two Children</li>
      <li>Pay Just The Taxes &amp; Fees</li>
    </ul>
    <ul class="feature-list features-right">
      <li>Multiple Travel Date Requests Allowed</li>
      <li>Fully Transferable To Another Person</li>
      <li>Just A 30 Days Advance Notice Required</li>
      <li>You Will Have 12 Months To Complete Travel After Redemption</li>
    </ul>

    <h2 class="section-tab tab-terms">TERMS AND CONDITIONS</h2>
    <p class="terms-copy">Keep in mind the examples I am uploading are simply to show you that they contain the "compliments of" and "exclusively for" elements. These must be included in new design. Please only use the content I provided in brief, dont use content from examples.</p>

    <div class="redeem-banner">
      <p class="call">VIEW ALL THE DETAILS OF THIS SPECIAL<br>OFFER AND REDEEM ONLINE AT</p>
      <p class="details">WWW.TOPAZVOUCHERDESK.COM<br>Certificate ID # 47261-38504<br>Expires 02/29/2020</p>
    </div>

    <section class="compliments-panel">
      <h3 class="panel-label">COMPLIMENTS OF</h3>
    </section>
    <svg class="fold-strip" width="23" height="246" viewBox="0 0 23 246" aria-hidden="true">
      <polygon points="0,0 23,36 23,246 0,246" fill="var(--panel-fold)"/>
    </svg>
    <section class="exclusive-panel">
      <h3 class="panel-label">EXCLUSIVELY FOR</h3>
    </section>
  </main>
</body>
</html>
```